Levelgrade Floor Inspections

We provide inspections and consulting services on various floor coverings, e.g. carpet, hardwood, etc. We also do expert witness work for attorneys due to floor covering failures. We current have a logo, just need it incorporated into a new design. I have examples of cards I have found on the internet that capture my attention and make a statement. I have included our original business card, which in my opinion is terrible, but it does have our logo on it.

```html
<!DOCTYPE html>
<html lang="en">
<head>
<meta charset="utf-8">
<title>Levelgrade Floor Inspections – Business Card</title>
<link rel="stylesheet" href="https://fonts.googleapis.com/css2?family=Lato:wght@400;700;900&display=swap">
<style>
  :root {
    --ink: #0b0c0d;
    --orange: #e05f24;
    --white: #ffffff;
    --paper: #ffffff;
  }
  * { margin: 0; padding: 0; box-sizing: border-box; }
  html, body { width: 1200px; height: 1200px; overflow: hidden; background: var(--paper); }
  body { position: relative; font-family: "Lato", Arial, sans-serif; }

  .card {
    position: absolute;
    left: 192px;
    width: 821px;
    height: 463px;
    background: var(--ink);
    overflow: hidden;
  }
  .card--front { top: 130px; }
  .card--back { top: 612px; }

  .brand-mark {
    position: absolute;
    border-radius: 50%;
    background: var(--orange);
    display: flex;
    align-items: center;
    justify-content: center;
    color: var(--ink);
    font-weight: 900;
    letter-spacing: 0.04em;
  }
  .card--front .brand-mark {
    width: 288px; height: 288px;
    left: 266px; top: 88px;
    font-size: 36px;
  }
  .card--back .brand-mark {
    width: 168px; height: 168px;
    left: 86px; top: 50px;
    font-size: 21px;
  }

  .name-band {
    position: absolute;
    left: 0; top: 259px;
    width: 318px; height: 71px;
    background: var(--orange);
    clip-path: polygon(0 0, 100% 0, 94% 100%, 0 100%);
  }
  .name-band__text {
    position: absolute;
    left: 26px; top: 50%;
    transform: translateY(-50%);
    font-size: 31px;
    font-weight: 700;
    color: var(--ink);
    white-space: nowrap;
  }

  .info-panel {
    position: absolute;
    inset: 0;
    background: var(--orange);
    clip-path: polygon(398px 0, 821px 0, 821px 463px, 270px 463px);
  }
  .company-title {
    position: absolute;
    right: 51px; top: 94px;
    text-align: right;
    color: var(--white);
    font-weight: 700;
    font-size: 32px;
    line-height: 40px;
    letter-spacing: 0.01em;
  }
  .contact-list {
    position: absolute;
    right: 51px; top: 283px;
    list-style: none;
    text-align: right;
    color: var(--white);
    font-size: 27px;
    line-height: 41px;
  }
  .contact-list li { display: flex; justify-content: flex-end; align-items: center; gap: 9px; }
  .contact-list svg { width: 22px; height: 22px; flex: none; }
</style>
</head>
<body>
  <section class="card card--front">
    <div class="brand-mark">LEVELGRADE</div>
  </section>

  <section class="card card--back">
    <div class="brand-mark">LEVELGRADE</div>
    <div class="name-band"><span class="name-band__text">DANA MERCER</span></div>
    <div class="info-panel">
      <h1 class="company-title">LEVELGRADE FLOOR<br>INSPECTIONS</h1>
      <ul class="contact-list">
        <li>303-555-0142
          <svg viewBox="0 0 24 24" aria-hidden="true"><rect x="6" y="2" width="12" height="20" rx="2.5" fill="none" stroke="#0b0c0d" stroke-width="2.4"/><circle cx="12" cy="17.5" r="1.4" fill="#0b0c0d"/></svg>
        </li>
        <li>dana@levelgradefloors.com
          <svg viewBox="0 0 24 24" aria-hidden="true"><rect x="2" y="5" width="20" height="14" rx="1.5" fill="#0b0c0d"/><path d="M3 6l9 7 9-7M3 18l7-6M21 18l-7-6" fill="none" stroke="#e05f24" stroke-width="1.4"/></svg>
        </li>
        <li>levelgradefloors.com
          <svg viewBox="0 0 24 24" aria-hidden="true"><circle cx="12" cy="12" r="10" fill="#0b0c0d"/><g fill="none" stroke="#e05f24" stroke-width="1.3"><ellipse cx="12" cy="12" rx="4" ry="9"/><path d="M3 12h18M4.5 7.5h15M4.5 16.5h15M12 3v18"/></g></svg>
        </li>
      </ul>
    </div>
  </section>
</body>
</html>
```